Velkano Holdings Ltd - An invesmtent & trading company needs a web design

We need a web design for our company based in Cyprus. The company was founded in 2009. We have continuously grown and now invest & trade all over the world.

Velkano Holdings ltd. specializes in the buying and selling of crude oil, precious metals and the investment in properties.

We know that trust is of the utmost importance when it comes to business and the design should communicate this to prospective business partners. Find attached the company logo. The colour scheme for the website should use similar colours and ideally incorporate the logo in some shape or form as well.

Target Market(s)

Oil Traders, Metall Traders, Property Investments

Industry/Entity Type

Trade

Coding

Coded - Design and coding required

Number of Pages Required

4 page

Font styles to use
Sans Serif

Requirements
Must have
• Mainpage,
• About Us
• Partners
• Legal Notice

```html
<!DOCTYPE html>
<html lang="en">
<head>
<meta charset="utf-8">
<title>Velkano Holdings Ltd</title>
<link rel="stylesheet" href="https://fonts.googleapis.com/css2?family=Open+Sans:wght@400;600;700;800&display=swap">
<style>
:root{
  --cyan:#35bfe0;
  --cyan-dark:#22a6c8;
  --cyan-deep:#1a93b5;
  --navy:#1c3553;
  --navy-deep:#14263c;
  --ink:#3a4450;
  --muted:#8a949e;
  --light:#f1f3f5;
  --line:#d7dde2;
  --white:#ffffff;
}
*{box-sizing:border-box;margin:0;padding:0}
html,body{width:791px;height:1200px;overflow:hidden;background:var(--white)}
body{font-family:"Open Sans",Arial,sans-serif;color:var(--ink);position:relative}
.abs{position:absolute}

/* header */
.site-header{left:0;top:0;width:791px;height:58px;background:var(--cyan);z-index:3}
.brand{left:14px;top:9px;display:flex;align-items:center;gap:8px}
.brand-square{width:38px;height:38px;background:var(--white)}
.brand-name{color:var(--white);font-weight:800;line-height:1;text-transform:uppercase}
.brand-name .l1{display:block;font-size:23px;letter-spacing:.5px}
.brand-name .l2{display:block;font-size:11.5px;letter-spacing:.4px;margin-top:2px}
.main-nav{left:366px;top:21px;display:flex;gap:6px}
.main-nav a{display:block;font-size:8px;font-weight:600;color:var(--white);text-decoration:none;padding:4px 10px;letter-spacing:.4px}
.main-nav a.active{background:var(--white);color:var(--cyan)}
.social-top{left:704px;top:21px;display:flex;gap:12px}
.social-top span{width:17px;height:17px;border:1.5px solid var(--white);border-radius:50%}

/* hero */
.hero{left:0;top:58px;width:791px;height:377px;background:linear-gradient(120deg,#c9ccd0 0%,#eef0f2 35%,#f7f7f7 55%,#b7bcc2 100%)}
.slide-panel{left:435px;top:158px;width:317px;height:145px;background:rgba(28,53,83,.62);padding:16px 18px;color:var(--white)}
.slide-panel h2{font-size:20px;font-weight:800;letter-spacing:.5px;text-transform:uppercase}
.slide-panel p{font-size:7.5px;line-height:1.55;margin-top:8px;text-align:right}
.btn{display:inline-block;font-size:7px;font-weight:700;letter-spacing:.4px;padding:6px 12px;text-transform:uppercase}
.btn-cyan{background:var(--cyan);color:var(--white)}
.slide-panel .btn{position:absolute;right:14px;bottom:14px}
.slide-dots{left:536px;top:292px;display:flex;gap:6px}
.slide-dots span{width:6px;height:6px;border-radius:50%;background:rgba(255,255,255,.6)}
.slide-dots span.on{background:var(--white)}

/* features */
.feature{top:461px;width:226px;height:185px;text-align:center;padding-top:16px}
.feature.boxed{border:1.5px solid var(--line)}
.feature-icon{width:30px;height:30px;margin:0 auto;background:var(--cyan);border-radius:3px;display:flex;align-items:center;justify-content:center}
.feature-icon.outline{background:var(--white);border:2px solid var(--cyan)}
.feature h3{font-size:10.5px;font-weight:700;color:var(--cyan);margin-top:14px;letter-spacing:.3px}
.feature p{font-size:6.5px;line-height:1.6;color:var(--muted);margin:8px auto 0;width:180px}
.btn-outline{border:1px solid var(--ink);color:var(--ink);margin-top:14px;padding:5px 12px}
.feature.boxed .btn-outline{background:var(--cyan);border-color:var(--cyan);color:var(--white)}

/* welcome */
.welcome{left:0;top:672px;width:791px;height:172px;background:var(--light);text-align:center;padding-top:26px}
.welcome h2{font-size:21px;font-weight:800;color:var(--navy);letter-spacing:.3px}
.welcome h2 span{color:var(--cyan)}
.welcome p{font-size:7px;line-height:1.65;color:var(--muted);width:650px;margin:12px auto 0}
.btn-navy{background:var(--navy);color:var(--white);margin-top:16px;padding:6px 16px}

/* partners */
.partners{left:0;top:878px;width:791px;height:63px}
.partner-arrow{top:20px;width:16px;height:24px;background:#e3e6e9;display:flex;align-items:center;justify-content:center}
.partner-badge{top:8px;width:110px;height:47px;border:1px solid var(--line);display:flex;align-items:center;justify-content:center}
.partner-badge span{display:block;width:70px;height:16px;background:#c5ccd3;border-radius:2px}

/* footer */
.site-footer{left:0;top:962px;width:791px;height:198px;background:var(--cyan);color:var(--white)}
.f-col{top:0;height:198px;padding:18px 18px 0}
.f-col h4{font-size:9.5px;font-weight:700;letter-spacing:.5px;margin-bottom:10px}
.f-col p{font-size:6.5px;line-height:1.65}
.f-newsletter{background:var(--cyan-deep)}
.f-input{width:100%;height:20px;background:var(--white);margin-top:10px;font-size:6.5px;color:var(--muted);padding:5px 8px}
.btn-sub{display:block;width:100%;text-align:center;background:var(--navy);color:var(--white);margin-top:6px;padding:6px 0}
.btn-white{background:var(--white);color:var(--cyan);margin-top:12px}
.contact-row{display:flex;align-items:flex-start;gap:7px;font-size:6.5px;line-height:1.5;margin-bottom:8px}
.follow-row{display:flex;align-items:center;gap:8px;font-size:7px;font-weight:600;margin-bottom:9px}
.follow-row span{width:16px;height:16px;background:var(--white)}
.bottom-bar{left:0;top:1160px;width:791px;height:40px;background:var(--navy-deep);color:#9fb0c2;font-size:6.5px;text-align:center;line-height:40px}
</style>
</head>
<body>

<header class="site-header abs">
  <div class="brand abs">
    <span class="brand-square"></span>
    <span class="brand-name"><span class="l1">Velkano</span><span class="l2">Holdings Ltd</span></span>
  </div>
  <nav class="main-nav abs">
    <a class="active" href="#">HOME</a>
    <a href="#">ABOUT US</a>
    <a href="#">PARTNERS</a>
    <a href="#">LEGAL NOTICE</a>
  </nav>
  <div class="social-top abs"><span></span><span></span></div>
</header>

<section class="hero abs" role="img" aria-label="Business people reviewing financial charts and documents at a desk"></section>

<div class="slide-panel abs">
  <h2>Velkano Holdings Ltd</h2>
  <p>Lorem ipsum dolor sit amet, consectetur adipiscing elit, sed do eiusmod tempor incididunt ut labore et dolore magna aliqua. Ut enim ad minim veniam, quis nostrud exercitation ullamco.</p>
  <span class="btn btn-cyan">Read More</span>
</div>
<div class="slide-dots abs"><span class="on"></span><span></span><span></span></div>

<section class="feature boxed abs" style="left:36px">
  <div class="feature-icon"><svg width="12" height="16" viewBox="0 0 12 16"><path d="M6 1 C6 1 1 8 1 10.5 A5 5 0 0 0 11 10.5 C11 8 6 1 6 1Z" fill="#fff"/></svg></div>
  <h3>LOREM IPSUM DOLOR</h3>
  <p>Lorem ipsum dolor sit amet, consectetur adipiscing elit, sed do eiusmod tempor incididunt ut labore et dolore magna.</p>
  <span class="btn btn-outline">Read More</span>
</section>
<section class="feature abs" style="left:282px">
  <div class="feature-icon outline"><svg width="12" height="16" viewBox="0 0 12 16"><text x="6" y="13" text-anchor="middle" font-family="Open Sans,sans-serif" font-size="14" font-weight="700" fill="#35bfe0">$</text></svg></div>
  <h3>LOREM IPSUM DOLOR</h3>
  <p>Lorem ipsum dolor sit amet, consectetur adipiscing elit, sed do eiusmod tempor incididunt ut labore et dolore magna.</p>
  <span class="btn btn-outline">Read More</span>
</section>
<section class="feature abs" style="left:526px">
  <div class="feature-icon outline"><svg width="14" height="14" viewBox="0 0 14 14"><rect x="2" y="2" width="10" height="10" fill="none" stroke="#35bfe0" stroke-width="2"/><path d="M5 7h4M7 5v4" stroke="#35bfe0" stroke-width="1.5"/></svg></div>
  <h3>LOREM IPSUM DOLOR</h3>
  <p>Lorem ipsum dolor sit amet, consectetur adipiscing elit, sed do eiusmod tempor incididunt ut labore et dolore magna.</p>
  <span class="btn btn-outline">Read More</span>
</section>

<section class="welcome abs">
  <h2>WELCOME TO VELKANO <span>HOLDINGS LTD</span></h2>
  <p>Lorem ipsum dolor sit amet, consectetur adipiscing elit, sed do eiusmod tempor incididunt ut labore et dolore magna aliqua. Ut enim ad minim veniam, quis nostrud exercitation ullamco laboris nisi ut aliquip ex ea commodo consequat. Duis aute irure dolor in reprehenderit in voluptate velit esse cillum dolore eu fugiat nulla pariatur. Excepteur sint occaecat cupidatat non proident, sunt in culpa qui officia deserunt mollit anim id est laborum.</p>
  <span class="btn btn-navy">Read More</span>
</section>

<section class="partners abs">
  <div class="partner-arrow abs" style="left:28px"><svg width="6" height="10" viewBox="0 0 6 10"><path d="M5 1 1 5l4 4" fill="none" stroke="#6b7680" stroke-width="1.5"/></svg></div>
  <div class="partner-badge abs" style="left:60px"><span></span></div>
  <div class="partner-badge abs" style="left:196px"><span></span></div>
  <div class="partner-badge abs" style="left:332px"><span></span></div>
  <div class="partner-badge abs" style="left:468px"><span></span></div>
  <div class="partner-badge abs" style="left:604px"><span></span></div>
  <div class="partner-arrow abs" style="left:746px"><svg width="6" height="10" viewBox="0 0 6 10"><path d="M1 1l4 4-4 4" fill="none" stroke="#6b7680" stroke-width="1.5"/></svg></div>
</section>

<footer class="site-footer abs">
  <div class="f-col abs" style="left:14px;width:240px">
    <h4>ABOUT US</h4>
    <p>Lorem ipsum dolor sit amet, consectetur adipiscing elit, sed do eiusmod tempor incididunt ut labore et dolore magna aliqua. Ut enim ad minim veniam, quis nostrud exercitation ullamco laboris nisi ut aliquip.</p>
    <span class="btn btn-white">Read More</span>
  </div>
  <div class="f-col f-newsletter abs" style="left:262px;width:208px">
    <h4>NEWSLETTER SIGNUP</h4>
    <p>Subscribe to our newsletter to receive our latest updates and market news.</p>
    <div class="f-input">Enter your email</div>
    <span class="btn btn-sub">Subscribe</span>
  </div>
  <div class="f-col abs" style="left:486px;width:180px">
    <h4>LOCATION</h4>
    <div class="contact-row"><svg width="8" height="10" viewBox="0 0 8 10"><path d="M4 0a3.5 3.5 0 0 0-3.5 3.5C.5 6 4 10 4 10s3.5-4 3.5-6.5A3.5 3.5 0 0 0 4 0Z" fill="#fff"/></svg><span>Harbour Road 14, Marina Quarter<br>Limassol 3045, Cyprus</span></div>
    <div class="contact-row"><svg width="8" height="9" viewBox="0 0 8 9"><path d="M1 0h2l1 2-1.3 1a5 5 0 0 0 2.3 2.3L6 4l2 1v2c0 1-1 2-2 2A7 7 0 0 1 0 2C0 1 0 0 1 0Z" fill="#fff"/></svg><span>+357 25 000 418</span></div>
    <div class="contact-row"><svg width="9" height="7" viewBox="0 0 9 7"><rect width="9" height="7" fill="#fff"/><path d="M0 0l4.5 3.5L9 0" fill="none" stroke="#35bfe0" stroke-width="1"/></svg><span>info@velkanoholdings.com</span></div>
  </div>
  <div class="f-col abs" style="left:670px;width:121px">
    <h4>FOLLOW US</h4>
    <div class="follow-row"><span></span>Friendline</div>
    <div class="follow-row"><span></span>Chirpwire</div>
    <div class="follow-row"><span></span>Proflink</div>
  </div>
</footer>

<div class="bottom-bar abs">Copyright © Velkano Holdings ltd. All rights reserved.</div>

</body>
</html>
```